Intenational Rhythmic Gymnastics Frostline Trophy

We need a poster for our new annual international rhythmic gymnastics competition "Frostline Trophy". Dates are December 21 -23, 2019.Picture we would like to use is attached.We would like to see holidays colors in the poster.It should have words "international rhythmic gymnastics", Name of the competition "Frostline Trophy" and dates.Also we would like for it to say somewhere that it is in Los Angeles, California, USAIt should have information about our club on the bottom of the poster like on the file attached (hosted by Venmarra Gymnastics with logo and address and website info)We also need a flyer that ties into the poster in look and colors with empty space below so we can add directives.We would like end product to be in file format that we can edit next year when the dates change.

Target Market(s)

Rhythmic Gymnastics Clubs

Industry/Entity Type

Gym

Colors

Designer to choose colors to be used in the design.

Requirements
Must have
• Picture we uploaded and all info we requested.
• Bright holiday colors

```html
<!DOCTYPE html>
<html lang="en">
<head>
<meta charset="utf-8">
<title>Frostline Trophy Poster</title>
<link href="https://fonts.googleapis.com/css2?family=Jost:wght@300;400&display=swap" rel="stylesheet">
<style>
  :root {
    --backdrop: #1f1f1f;
    --navy: #1c2352;
    --navy-deep: #171d47;
    --white: #ffffff;
    --lilac: #9a72c4;
    --band: #8458ab;
    --studio-light: #d6ccc4;
    --studio-mid: #bcafa6;
    --studio-warm: #8c7c70;
    --ribbon-blue: #2b3fae;
    --ribbon-teal: #3fbfd8;
    --ribbon-violet: #6a3fc0;
    --skin: #c9906e;
    --leotard: #4a3a7a;
  }
  html, body {
    margin: 0;
    padding: 0;
    width: 1200px;
    height: 1200px;
    overflow: hidden;
    background: var(--backdrop);
    font-family: "Jost", "Futura", sans-serif;
  }
  .poster {
    position: absolute;
    left: 247px;
    top: 114px;
    width: 714px;
    height: 1000px;
    overflow: hidden;
  }
  .studio-backdrop {
    position: absolute;
    inset: 0;
    background:
      radial-gradient(ellipse at 75% 70%, var(--studio-light) 0%, transparent 60%),
      linear-gradient(160deg, var(--studio-mid) 0%, var(--studio-light) 45%, var(--studio-mid) 75%, var(--studio-warm) 100%);
  }
  .gymnast-photo {
    position: absolute;
    left: 0;
    top: 160px;
    width: 714px;
    height: 808px;
    background:
      radial-gradient(ellipse 26% 20% at 50% 72%, var(--leotard) 0%, transparent 100%),
      radial-gradient(ellipse 55% 22% at 55% 82%, var(--skin) 0%, transparent 100%),
      radial-gradient(ellipse 22% 50% at 14% 45%, var(--ribbon-blue) 0%, transparent 100%),
      radial-gradient(ellipse 14% 35% at 8% 35%, var(--ribbon-teal) 0%, transparent 100%),
      radial-gradient(ellipse 18% 20% at 30% 72%, var(--ribbon-violet) 0%, transparent 100%);
    opacity: 0.75;
  }
  .title-disc {
    position: absolute;
    left: 83px;
    top: 24px;
    width: 540px;
    height: 540px;
    box-sizing: border-box;
    border-radius: 50%;
    background: radial-gradient(circle at 50% 40%, var(--navy) 0%, var(--navy-deep) 100%);
    border: 2px solid var(--white);
    color: var(--white);
    text-align: center;
  }
  .disc-line {
    position: absolute;
    left: 0;
    right: 0;
    margin: 0;
    line-height: 1;
  }
  .club-name {
    top: 80px;
    font-size: 26px;
    font-weight: 400;
  }
  .event-kicker {
    top: 136px;
    font-size: 24px;
    font-weight: 400;
    letter-spacing: 0.3px;
  }
  .event-name {
    font-size: 108px;
    font-weight: 300;
  }
  .event-name-first { top: 164px; }
  .event-name-second { top: 280px; }
  .event-dates {
    top: 428px;
    left: 50%;
    right: auto;
    transform: translateX(-50%);
    padding: 0 16px;
    height: 32px;
    line-height: 32px;
    border-radius: 16px;
    background: var(--lilac);
    font-size: 27px;
    font-weight: 300;
    white-space: nowrap;
  }
  .event-place {
    top: 472px;
    font-size: 26px;
    font-weight: 400;
  }
  .site-band {
    position: absolute;
    left: 0;
    right: 0;
    bottom: 0;
    height: 32px;
    line-height: 32px;
    background: var(--band);
    color: var(--white);
    text-align: center;
    font-size: 19px;
    font-weight: 400;
  }
</style>
</head>
<body>
  <main class="poster">
    <div class="studio-backdrop"></div>
    <div class="gymnast-photo" role="img" aria-label="Photo of a rhythmic gymnast in a jewelled purple leotard lunging backwards while swirling a blue, teal and purple ribbon"></div>

    <section class="title-disc">
      <p class="disc-line club-name">Venmarra Gymnastics</p>
      <p class="disc-line event-kicker">International Rhythmic Gymnastics</p>
      <h1 class="disc-line event-name event-name-first">Frostline</h1>
      <p class="disc-line event-name event-name-second">Trophy</p>
      <p class="disc-line event-dates">Dec 21-23 | 2019</p>
      <p class="disc-line event-place">Los Angeles,California</p>
    </section>

    <footer class="site-band">venmarragymnastics.com</footer>
  </main>
</body>
</html>
```